Brindle Works Ltd

I'd like to create a company letterhead for the attached logo in word format.

I'd like to emphasis the icon in large translucent state from the left corner and ensure that the letterhead colouring matches the colour palette of the current logo with a contrast so it's clear to see. I've attached a copy of our sister company page on the app for reference.

```html
<!DOCTYPE html>
<html lang="en">
<head>
<meta charset="utf-8">
<title>Brindle Works Ltd — Letterhead</title>
<link rel="stylesheet" href="https://fonts.googleapis.com/css2?family=Montserrat:wght@400&family=Roboto:wght@400&display=swap">
<style>
  :root {
    --teal: #1ab3a0;
    --teal-faint: #e6f2f1;
    --grey-band: #999999;
    --text-grey: #6b6b6b;
    --paper: #f8f8f8;
    --backdrop: #dcdcdc;
  }
  * { margin: 0; padding: 0; box-sizing: border-box; }
  html, body {
    width: 1153px;
    height: 1200px;
    overflow: hidden;
    background: var(--backdrop);
  }
  .letterhead {
    position: absolute;
    left: 176px;
    top: 40px;
    width: 800px;
    height: 1120px;
    background: var(--paper);
    overflow: hidden;
  }
  .backdrop-mark {
    position: absolute;
    left: 133px;
    top: 357px;
    width: 532px;
    height: 532px;
    border-radius: 50%;
    background: var(--teal-faint);
  }
  .brand-name {
    position: absolute;
    left: 71px;
    top: 70px;
    font-family: "Montserrat", sans-serif;
    font-weight: 400;
    font-size: 26px;
    line-height: 1;
    color: var(--teal);
    white-space: nowrap;
  }
  .address, .contact {
    position: absolute;
    top: 62px;
    font-family: "Roboto", sans-serif;
    font-size: 14.5px;
    line-height: 18px;
    color: var(--text-grey);
    list-style: none;
    font-style: normal;
  }
  .address { left: 355px; }
  .contact { left: 551px; }
  .contact li {
    display: flex;
    align-items: center;
    gap: 6px;
  }
  .contact-icon {
    width: 12px;
    height: 12px;
    flex: none;
  }
  .footer-band {
    position: absolute;
    left: 0;
    bottom: 0;
    width: 800px;
    height: 17px;
  }
</style>
</head>
<body>
  <main class="letterhead">
    <div class="backdrop-mark" aria-hidden="true"></div>

    <header>
      <div class="brand-name">Brindle Works Ltd</div>

      <address class="address">
        Brindle Works Ltd<br>
        48 Harrow Mill Lane Unit<br>
        7 Fairbrook, OR 97214
      </address>

      <ul class="contact">
        <li>
          <svg class="contact-icon" viewBox="0 0 12 12" aria-hidden="true">
            <path d="M1 4.5 C1 2.5 3 2 6 2 C9 2 11 2.5 11 4.5 L8.5 5 L8 3.8 H4 L3.5 5 Z" fill="var(--teal)"/>
            <path d="M3 6 H9 L10 10 H2 Z" fill="var(--teal)"/>
            <circle cx="6" cy="8" r="1.2" fill="var(--paper)"/>
          </svg>
          1-800-555-0147
        </li>
        <li>
          <svg class="contact-icon" viewBox="0 0 12 12" aria-hidden="true">
            <rect x="0.5" y="2.5" width="11" height="7" fill="var(--teal)"/>
            <path d="M0.8 2.8 L6 6.6 L11.2 2.8" fill="none" stroke="var(--paper)" stroke-width="1"/>
            <path d="M0.8 9.2 L4.5 5.6 M11.2 9.2 L7.5 5.6" stroke="var(--paper)" stroke-width="0.8"/>
          </svg>
          hello@brindleworks.co
        </li>
        <li>
          <svg class="contact-icon" viewBox="0 0 12 12" aria-hidden="true">
            <circle cx="6" cy="6" r="5.5" fill="var(--teal)"/>
            <path d="M3 3 C4.5 3.5 4 5 5 5.5 C6 6 5 8 6 9.5 M8 2.5 C7.5 4 9 4.5 9.5 6" fill="none" stroke="var(--paper)" stroke-width="1.1"/>
          </svg>
          www.brindleworks.co
        </li>
      </ul>
    </header>

    <svg class="footer-band" viewBox="0 0 800 17" aria-hidden="true">
      <polygon points="0,0 576,0 559,17 0,17" fill="var(--teal)"/>
      <polygon points="580,17 597,0 800,0 800,17" fill="var(--grey-band)"/>
    </svg>
  </main>
</body>
</html>
```